Cinq Leviers SEO Zorvana Plumea ebook cover (2nd of book series) *

Book Title :
Cinq Leviers pour muscler votre Visibilité Organique SEO

Or alternatively if design is better :
SEO : Cinq Leviers pour muscler votre Visibilité Organique

Subtitle : Comment hisser votre page au sommet des annuaires du web

Subject : The book is a very practical how-to guide to help anyone increase dramatically their trafic through SEO (Search Engine Opimization)

It is written in French : so please keep punctuation as provided

The book cover MUST STAND OUT on the Zorvana Plateform as a small Thumbnail (The important words must be readable even at that size : CINQ LEVIERS, Visibilité Organique, SEO) as well as a 6*9 book.

The imagery should make the viewer feel that the book (and the author) are the authority in Search Engine Optimization and Digital Marketing

The readers should feel that they must have this book to increase their site or blog traffic fast.

It is most important that the book “pops off the shelf” and catches the eye quickly. The most important part of the design is that it sells, not that it looks pretty (but it can :-)

Important thing : this cover and ebook is part of a series of books all titled “Cinq Leviers blablabla”. There is already one book of this series published (see cover 5) : Cinq Leviers pour Doubler vos Gains. It’s important that at least one element of this new design recalls the design of the Cover 5 It can be for example the typo for the “7” being the same, or any other idea so that when someone sees both covers, they understand they are from the same series.

I have also enclosed my attempt so that you get the idea I am after, but don’t be too close to it. I am not a designer and I know it is bad, so be free, it is just here to explain the idea of the book cover.
Attached are some covers :
 Covers 1 to 4 are covers I like very much
 Cover 5 is from The first book of the Series : “Cinq Leviers pour Doubler vos Gains” : there should be at least ONE (even tiny) element in common with the new design so that it’s clear they belong to the same series
 Cover 6 is my ugly attempt so that the idea is clear (hopefully)

Target Market(s)

Small entrepreneurs bloggers

Font styles to use
Sans Serif

Colors

Designer to choose colors to be used in the design.

Requirements
Must have
• The book cover MUST STAND OUT on the Zorvana Plateform as a small Thumbnail (The important must be readable even at that size : CINQ LEVIERS, Visibilité Organique, SEO) as well as a 6*9 book.
• Important thing : this cover and ebook is part of a series of books all titled “Cinq Leviers blablabla”. There is already one book of this series published (see cover 5) : Cinq Leviers pour Doubler vos Gains. It’s important that at least one element of this new design recalls the design of the Cover 5 It can be for example the typo for the “7” being the same, or any other idea so that when someone sees both covers, they understand they are from the same series.
• All the texts provided on the brief and my sample cover (6th cover mockup)
• Please enclose the text :
• Checklist SEO Incluse
• In a sticker (see last image as example)
Nice to have
• Nice and simple imagery. Like the one on Cart Sparks. Very simple but also very powerful and meaningful
Should not have
• It should not be as cluttered as my attempt (6th cover enclosed)

```html
<!DOCTYPE html>
<html lang="fr">
<head>
<meta charset="utf-8">
<title>Cinq Leviers pour muscler votre Visibilité Organique</title>
<link rel="stylesheet" href="https://fonts.googleapis.com/css2?family=Ultra&family=Arvo:wght@400;700&family=Libre+Baskerville:wght@400;700&family=Rubik:ital,wght@1,900&display=swap">
<style>
  :root {
    --orange: #fb6a3a;
    --ink: #2b2b2b;
    --grey: #5a5a55;
    --rule: #4a4a4a;
    --paper: #ffffff;
    --art-light: #e6eff1;
    --art-mid: #c9dde2;
  }
  * { margin: 0; padding: 0; box-sizing: border-box; }
  html, body { width: 840px; height: 1200px; overflow: hidden; background: var(--paper); }
  .cover { position: relative; width: 840px; height: 1200px; background: var(--paper); overflow: hidden; }
  .title-art { position: absolute; left: 0; top: 0; width: 840px; height: 590px; overflow: visible; }
  .title-word {
    font-family: "Ultra", serif;
    fill: var(--orange);
    stroke: #1f1f1f;
    stroke-width: 1.2;
    paint-order: stroke;
    filter: drop-shadow(3px 3px 0 #333);
  }
  .title-link { font-family: "Arvo", serif; fill: var(--ink); }
  .hero-art {
    position: absolute; left: 236px; top: 572px; width: 372px; height: 292px;
    border-radius: 50%;
    background: radial-gradient(circle at 50% 55%, var(--art-mid) 0%, var(--art-light) 55%, rgba(255,255,255,0) 72%);
  }
  .sticker { position: absolute; left: 12px; top: 722px; width: 196px; height: 196px; }
  .sticker-text { font-family: "Rubik", sans-serif; font-style: italic; font-weight: 900; fill: #fff; }
  .rule { position: absolute; left: 58px; width: 736px; height: 1px; background: var(--rule); }
  .rule.top { top: 948px; }
  .rule.bottom { top: 1048px; }
  .subtitle {
    position: absolute; left: 58px; top: 954px; width: 736px;
    font-family: "Libre Baskerville", serif; font-size: 33px; line-height: 42px;
    color: var(--grey); text-align: center;
  }
  .subtitle .accent { color: var(--orange); }
  .author {
    position: absolute; left: 0; top: 1066px; width: 840px; text-align: center;
    font-family: "Libre Baskerville", serif; font-weight: 700; font-size: 34px; letter-spacing: 1px;
    color: var(--orange); text-shadow: 1px 1px 0 #333;
  }
  .banner {
    position: absolute; left: 0; top: 1122px; width: 840px; height: 52px;
    background: var(--orange); box-shadow: 0 3px 4px rgba(0,0,0,.35);
    display: flex; align-items: center; justify-content: center;
    font-family: "Libre Baskerville", serif; font-weight: 700; font-size: 31px; letter-spacing: 1px;
    color: #fff; text-shadow: 1px 1px 0 #222;
  }
</style>
</head>
<body>
<main class="cover">
  <svg class="title-art" viewBox="0 0 840 590" aria-label="Cinq Leviers pour muscler votre Visibilité Organique">
    <text class="title-word" x="20" y="196" font-size="150" textLength="250" lengthAdjust="spacingAndGlyphs">CINQ</text>
    <text class="title-word" x="292" y="144" font-size="118" textLength="524" lengthAdjust="spacingAndGlyphs">LEVIERS</text>
    <text class="title-link" x="292" y="232" font-size="54" textLength="524" lengthAdjust="spacingAndGlyphs">pour muscler votre</text>
    <text class="title-word" x="22" y="370" font-size="110" textLength="796" lengthAdjust="spacingAndGlyphs">VISIBILITÉ</text>
    <text class="title-word" x="92" y="526" font-size="138" textLength="676" lengthAdjust="spacingAndGlyphs">ORGANIQUE</text>
  </svg>

  <div class="hero-art" role="img" aria-label="Illustration SEO : écran d'ordinateur marqué SEO, fusée, pièces, cible et graphiques sur fond de globe"></div>

  <svg class="sticker" viewBox="0 0 200 200" aria-label="Checklist SEO incluse">
    <g transform="rotate(18 100 100)">
      <polygon fill="var(--orange)" filter="drop-shadow(2px 3px 2px rgba(0,0,0,.35))"
        points="100,8 112,24 131,13 137,33 158,29 157,50 178,54 168,72 186,84 170,98 182,116 162,123 167,144 146,145 143,166 124,160 114,179 100,166 86,179 76,160 57,166 54,145 33,144 38,123 18,116 30,98 14,84 32,72 22,54 43,50 42,29 63,33 69,13 88,24"/>
      <rect x="14" y="70" width="172" height="58" fill="var(--grey)"/>
      <text class="sticker-text" x="100" y="60" font-size="20" text-anchor="middle">Checklist</text>
      <text class="sticker-text" x="100" y="121" font-size="56" text-anchor="middle" stroke="#333" stroke-width="2" paint-order="stroke">SEO</text>
      <text class="sticker-text" x="100" y="152" font-size="19" text-anchor="middle">Incluse</text>
    </g>
  </svg>

  <div class="rule top"></div>
  <p class="subtitle">Comment hisser votre page au <span class="accent">sommet</span><br>des annuaires du web</p>
  <div class="rule bottom"></div>

  <p class="author">MAXIME DURAVEL</p>

  <div class="banner">CHECKLIST SEO GRATUITE INCLUSE</div>
</main>
</body>
</html>
```